New career and executive coaching business needs a business card design including logo

Company name: 'Harborline Growth Partners.' The aim of my coaching engagements is to help people improve their communication in the workplace and achieve their career goals. The process involves working with individuals to help them uncover their strengths and talents, then leverage those to improve their working lives. The Tavelle Inventory is the starting point to the process. I am after an exciting and interesting business card design (including logo)which is professional yet will still get people's attention.

Industry/Entity Type

Business

Contact Information for Business Card

Name: Gordon Halvey
Position: Owner
Address: 58 Merrowind Cres, Donvale Vic 3111
Phone: 0481936045
Website: harborlinegrowth.com.au
Email: gordon@hgp.com.au

Colors
33a6d7
00a990
0355a3
3176b5

Requirements
Must have
• logo

```html
<!DOCTYPE html>
<html lang="en">
<head>
<meta charset="utf-8">
<title>Harborline Growth Partners – Business Card</title>
<link rel="stylesheet" href="https://fonts.googleapis.com/css2?family=Open+Sans:wght@400;600;700&display=swap">
<style>
  :root {
    --stage: #000000;
    --card-white: #ffffff;
    --card-blue: #0756a4;
    --card-blue-light: #0e5fae;
    --teal: #00a990;
    --ink: #1a1a1a;
    --badge: #d9dde2;
  }
  * { margin: 0; padding: 0; box-sizing: border-box; }
  html, body {
    width: 1200px; height: 900px; overflow: hidden;
    background: var(--stage);
    font-family: "Open Sans", Arial, sans-serif;
  }
  .canvas { position: relative; width: 1200px; height: 900px; }

  .card { position: absolute; width: 477px; height: 293px; overflow: hidden; }

  .card-front {
    left: 116px; top: 275px;
    background: var(--card-white);
    border-radius: 0 56px 0 56px;
  }
  .card-back {
    left: 622px; top: 276px;
    background: var(--card-blue);
    border-radius: 56px 0 56px 0;
  }

  .brand { position: absolute; display: flex; align-items: center; gap: 12px; }
  .brand-mark { width: 40px; height: 40px; background: var(--teal); flex: none; }
  .brand-name { font-weight: 600; font-size: 23px; letter-spacing: 0.2px; white-space: nowrap; }
  .card-front .brand { left: 33px; top: 33px; }
  .card-front .brand-name { color: var(--ink); }

  .holder { position: absolute; left: 35px; top: 123px; }
  .holder-name { color: var(--teal); font-weight: 700; font-size: 17px; line-height: 22px; }
  .holder-role { color: var(--ink); font-size: 13px; line-height: 18px; margin-top: 1px; }

  .contacts { position: absolute; left: 35px; top: 175px; list-style: none; }
  .contacts li {
    display: flex; align-items: center; gap: 6px;
    font-size: 13px; color: var(--ink); height: 19.5px;
  }
  .contacts svg { width: 10px; height: 10px; flex: none; }

  .badges { position: absolute; left: 34px; top: 247px; display: flex; gap: 17px; align-items: center; }
  .badge { background: var(--badge); border-radius: 3px; }
  .badge-a { width: 104px; height: 20px; }
  .badge-b { width: 74px; height: 18px; }

  .back-arc { position: absolute; left: 0; top: 0; }
  .card-back .brand { right: 42px; top: 203px; }
  .card-back .brand-name { color: var(--card-white); font-size: 25px; }
</style>
</head>
<body>
<div class="canvas">

  <section class="card card-front" aria-label="Business card front">
    <div class="brand">
      <span class="brand-mark" aria-hidden="true"></span>
      <span class="brand-name">Harborline Growth Partners</span>
    </div>

    <div class="holder">
      <p class="holder-name">Gordon Halvey</p>
      <p class="holder-role">Owner</p>
    </div>

    <ul class="contacts">
      <li>
        <svg viewBox="0 0 10 10" aria-hidden="true"><path fill="#00a990" d="M2 0.5 L3.6 2.6 L2.8 3.6 C3.4 5 4.9 6.5 6.4 7.2 L7.4 6.4 L9.5 8 L8.6 9.5 C4.5 9.3 0.7 5.5 0.5 1.4 Z"/></svg>
        <span>0481936045</span>
      </li>
      <li>
        <svg viewBox="0 0 10 10" aria-hidden="true"><rect x="0.5" y="2" width="9" height="6.5" fill="#00a990"/><path d="M0.8 2.3 L5 5.6 L9.2 2.3" stroke="#fff" stroke-width="0.9" fill="none"/></svg>
        <span>gordon@hgp.com.au</span>
      </li>
      <li>
        <svg viewBox="0 0 10 10" aria-hidden="true"><circle cx="5" cy="5" r="4.6" fill="#00a990"/><path d="M0.6 5 H9.4 M5 0.4 C2.6 3 2.6 7 5 9.6 M5 0.4 C7.4 3 7.4 7 5 9.6" stroke="#fff" stroke-width="0.7" fill="none"/></svg>
        <span>harborlinegrowth.com.au</span>
      </li>
    </ul>

    <div class="badges">
      <span class="badge badge-a" role="img" aria-label="Assessment partner badge"></span>
      <span class="badge badge-b" role="img" aria-label="Certified coach badge"></span>
    </div>
  </section>

  <section class="card card-back" aria-label="Business card back">
    <svg class="back-arc" width="477" height="293" viewBox="0 0 477 293" aria-hidden="true">
      <path d="M0 0 H175 C110 90 110 210 175 293 H0 Z" fill="#0a5aa8"/>
    </svg>
    <div class="brand">
      <span class="brand-name">Harborline Growth Partners</span>
    </div>
  </section>

</div>
</body>
</html>
```